cutest and professional business cards

I am looking at getting very good designs that will scream - contact this TEAM (7)
So could be that one or two awesome design and in variations for members of my team. Vector files are attached within the brief.
I will like the circle image (see vector-file) to be within the back of the cards as part of the design and the text "You're Creative - Join our Community"

Target Market(s)

Creative youths and millennials as well as very business/entrepreneurial minded community.

Contact Information for Business Card

logo,
name: for design1: Mirela Tasdo for design2,3,4,5,6,7: leave blank space to possibility to handprint/sign name
position: design1: Founder, design2,3,4,5,6,7: community relationship manager, Fullstack developer, software designer, digital marketer, financial and operating officer, creative intern
address: Workrooste - 42 Feltmore Ave Harlow Bay HB j4r 2m6
number: 705-8142-596
website: www.lomivarta.com
worklink -/lomivart
peoplepage - /lomivart
chirper - /lomivar
instagram -/lomivart

Font styles to use
Other font styles liked:
• monserratt

Requirements
Must have
• Font type: monserratt
• colours: off blue #1BBC9C , Red #BB2838
Nice to have
• a catchy, youthful and professional design
Should not have
• any additional colors besides dark grey and white.

```html
<!DOCTYPE html>
<html lang="en">
<head>
<meta charset="utf-8">
<title>Lomivarta business cards</title>
<link rel="stylesheet" href="https://fonts.googleapis.com/css2?family=Montserrat:wght@400;500;600;700&display=swap">
<style>
  :root {
    --teal: #1BBC9C;
    --red: #BB2838;
    --dark: #333333;
    --mid: #555555;
    --band: #e2e2e2;
    --paper: #ffffff;
    --page: #ffffff;
  }
  * { box-sizing: border-box; margin: 0; padding: 0; }
  html, body { width: 994px; height: 1200px; overflow: hidden; background: var(--page); }
  body { position: relative; font-family: "Montserrat", sans-serif; color: var(--dark); }

  .card {
    position: absolute;
    background: var(--paper);
    overflow: hidden;
    box-shadow: 4px 8px 18px rgba(0,0,0,0.35);
  }
  .card--front { left: 128px; top: 97px; width: 763px; height: 437px; }
  .card--back  { left: 128px; top: 631px; width: 754px; height: 437px; }

  .card__decor {
    position: absolute;
    left: -230px; top: 110px;
    width: 460px; height: 460px;
    border-radius: 50%;
    background: linear-gradient(180deg, #d8efea 0%, #d8efea 48%, #efcdc6 52%, #efcdc6 100%);
    opacity: 0.9;
  }

  .brand { position: absolute; display: flex; flex-direction: column; align-items: flex-end; }
  .brand__row { display: flex; align-items: center; gap: 14px; }
  .brand__dot { border-radius: 50%; background: var(--teal); flex: none; }
  .brand__name { font-weight: 700; color: var(--dark); line-height: 1; letter-spacing: -1px; }
  .brand__tagline { font-weight: 500; color: var(--dark); line-height: 1; }

  .card--front .brand { right: 34px; top: 238px; }
  .card--front .brand__dot { width: 58px; height: 58px; }
  .card--front .brand__name { font-size: 78px; }
  .card--front .brand__tagline { font-size: 28px; margin-top: 6px; }
  .front__url {
    position: absolute; right: 36px; top: 386px;
    font-size: 17px; letter-spacing: 8px; color: var(--dark);
  }

  .card--back .brand { left: 0; right: 0; top: 56px; align-items: center; }
  .card--back .brand__dot { width: 38px; height: 38px; }
  .card--back .brand__name { font-size: 52px; }
  .card--back .brand__tagline { font-size: 18px; margin-top: 4px; margin-left: 120px; }

  .person { position: absolute; left: 78px; top: 176px; }
  .person__name { font-size: 34px; font-weight: 700; color: var(--dark); line-height: 1.1; }
  .person__roles { font-size: 17px; color: var(--mid); line-height: 22px; margin-top: 4px; width: 620px; letter-spacing: -0.3px; }

  .contact { position: absolute; top: 287px; display: flex; gap: 8px; font-size: 17px; color: var(--mid); line-height: 22px; }
  .contact--address { left: 58px; }
  .contact--reach { left: 451px; }
  .contact__icons { display: flex; flex-direction: column; }
  .contact__icons svg { height: 22px; width: 14px; }

  .social {
    position: absolute; left: 0; right: 0; top: 365px; height: 44px;
    background: var(--band);
    display: flex; align-items: center; padding-left: 55px; gap: 28px;
    font-size: 16.5px; color: var(--red);
  }
  .social__item { display: flex; align-items: center; gap: 8px; white-space: nowrap; }
  .social__mark { width: 14px; height: 14px; background: var(--red); flex: none; }
</style>
</head>
<body>

  <section class="card card--front">
    <div class="card__decor" role="img" aria-label="Soft teal and blush decorative shape"></div>
    <div class="brand">
      <div class="brand__row">
        <span class="brand__dot"></span>
        <span class="brand__name">Lomivarta</span>
      </div>
      <span class="brand__tagline">Makers move Markets</span>
    </div>
    <p class="front__url">www.lomivarta.com</p>
  </section>

  <section class="card card--back">
    <div class="brand">
      <div class="brand__row">
        <span class="brand__dot"></span>
        <span class="brand__name">Lomivarta</span>
      </div>
      <span class="brand__tagline">Makers move Markets</span>
    </div>

    <div class="person">
      <h1 class="person__name">Mirela Tasdo</h1>
      <p class="person__roles">community relationship manager, Fullstack developer, software designer, digital marketer, financial and operating officer, creative intern</p>
    </div>

    <div class="contact contact--address">
      <div class="contact__icons">
        <svg viewBox="0 0 14 22" aria-hidden="true"><path d="M1 11 L7 5 L13 11 M3 10 V17 H11 V10" fill="none" stroke="var(--teal)" stroke-width="1.6"/></svg>
      </div>
      <p>Workrooste - 42 Feltmore<br>Ave Harlow Bay HB j4r 2m6</p>
    </div>

    <div class="contact contact--reach">
      <div class="contact__icons">
        <svg viewBox="0 0 14 22" aria-hidden="true"><rect x="3" y="4" width="7" height="12" rx="1.5" fill="var(--teal)"/><rect x="4.5" y="6" width="4" height="5" fill="#fff"/></svg>
        <svg viewBox="0 0 14 22" aria-hidden="true"><circle cx="7" cy="11" r="5" fill="none" stroke="var(--teal)" stroke-width="1.4"/><path d="M2 11 H12 M7 6 V16" stroke="var(--teal)" stroke-width="1.2"/></svg>
      </div>
      <p>705-8142-596<br>www.lomivarta.com</p>
    </div>

    <div class="social">
      <span class="social__item"><span class="social__mark"></span>worklink -/lomivart</span>
      <span class="social__item"><span class="social__mark"></span>peoplepage - /lomivart</span>
      <span class="social__item"><span class="social__mark"></span>chirper - /lomivar</span>
    </div>
  </section>

</body>
</html>
```